MS Word and MS Powerpoint template creation using existing logo as style guide

Create a professional looking MS Word document template and MS powerpoint template for Korvath Advisory Pty Ltd using a logo that's already been created as the style guide. Korvath is a professional services business providing strategy, governance and execution support to small and medium business, Boards and executive teams. refer design brief.

Target Market(s)

Small to medium business, Chairs, Boards, executive teams, general managers

Industry/Entity Type

Professional business services, consultancy, business support outsourcing

Font styles to use
Other font styles liked:
• calibri

Requirements
Must have
• leverage the existing logo for colour scheme. Use the KORVATH logo type font. Fully editable templates Word and MS Powerpoint,
Nice to have
• Refer to the design brief
Should not have
• animations, cartoons, stock images of people.

```html
<!DOCTYPE html>
<html lang="en">
<head>
<meta charset="utf-8">
<title>Korvath Advisory – Report and Presentation Templates</title>
<link rel="stylesheet" href="https://fonts.googleapis.com/css2?family=Arimo:wght@400;500;700&display=swap">
<style>
:root{
  --navy:#1b3247;
  --navy-soft:#2d4a66;
  --ink:#3b3e42;
  --paper:#ffffff;
  --bg:#dcdcdc;
  --grey:#8b8b8b;
  --grey-dark:#5f5f5f;
  --light:#ececec;
  --text:#2b2b2b;
}
*{box-sizing:border-box;margin:0;padding:0}
html,body{width:1200px;height:1182px;overflow:hidden}
body{background:var(--bg);font-family:'Arimo',Arial,sans-serif;color:var(--text)}
.canvas{position:relative;width:1200px;height:1182px}
.page,.slide{position:absolute;background:var(--paper);overflow:hidden;box-shadow:2px 3px 5px rgba(0,0,0,.28)}
.page{width:201px;height:284px}
.slide{width:324px;height:182px}
.abs{position:absolute}
.fill{position:absolute;left:0;top:0}
.label{position:absolute;font-size:4.6px;color:var(--navy);letter-spacing:.1px}
.copy{position:absolute;font-size:3.2px;line-height:1.35;color:var(--text)}
.copy p+p{margin-top:2.5px}
.caps{position:absolute;text-transform:uppercase;font-size:3.7px;line-height:1.3;color:#fff}
.wordmark{position:absolute;color:#fff;font-weight:400;letter-spacing:2px;text-align:center;line-height:1}
/* document footer */
.doc-foot{position:absolute;left:0;bottom:0;width:201px;height:22px}
.doc-foot .ref{position:absolute;left:15px;top:5px;font-size:2.4px;color:#fff}
.doc-foot .contact{position:absolute;left:15px;top:11px;font-size:2.4px;color:#fff;word-spacing:1px}
.doc-foot .rule{position:absolute;left:15px;top:16px;width:125px;height:.4px;background:rgba(255,255,255,.5)}
.doc-foot .mark{position:absolute;left:157px;top:8px;font-size:3.8px;letter-spacing:.8px;color:#fff}
/* slide name box */
.logo-box{position:absolute;left:291px;top:161px;width:33px;height:14px;background:var(--navy);color:#fff;text-align:center;font-size:3.8px;letter-spacing:.8px;line-height:14px}
.slide-title{position:absolute;left:17px;top:12px;font-size:8.3px;letter-spacing:.2px}
/* table */
.data-table{position:absolute;left:15px;top:28px;border-collapse:separate;border-spacing:1px 2px;font-size:3px}
.data-table td,.data-table th{height:5.4px;padding:0 2px;text-align:left;font-weight:400}
.data-table th{background:var(--navy);color:#fff}
.data-table th.first{background:var(--ink)}
.data-table td{background:var(--light)}
.data-table td.name{width:71px;background:#f3f3f3}
.data-table td.num,.data-table th.num{width:23px}
.legend{position:absolute;font-size:2.6px;color:var(--grey-dark)}
.legend i{display:inline-block;width:2px;height:2px;border-radius:50%;margin:0 1px 0 2px;vertical-align:middle}
.tick-item{position:absolute;left:122px;width:72px}
.tick-item .head{font-size:3px;color:var(--navy);display:flex;align-items:center;gap:2px}
.tick-item .copy{position:static;margin:3px 0 0 8px;font-size:2.9px}
.agenda-list{position:absolute;left:39px;top:35px;font-size:4.4px;line-height:7.8px;color:var(--navy)}
.agenda-nums{position:absolute;left:17px;top:35px;font-size:3.2px;line-height:7.8px;color:#fff}
.card-text{position:absolute;left:10px;top:40px;font-size:4.2px;line-height:1.2;color:#fff;text-transform:uppercase}
</style>
</head>
<body>
<div class="canvas">

<!-- ========== REPORT COVER ========== -->
<section class="page cover" style="left:71px;top:84px">
  <svg class="fill" width="201" height="284" viewBox="0 0 201 284">
    <defs>
      <linearGradient id="cityTop" x1="0" y1="0" x2="0" y2="1">
        <stop offset="0" stop-color="#c9d3de"/><stop offset=".55" stop-color="#6f8197"/><stop offset="1" stop-color="#3e536c"/>
      </linearGradient>
      <linearGradient id="cityLow" x1="0" y1="0" x2="1" y2="1">
        <stop offset="0" stop-color="#7487a0"/><stop offset="1" stop-color="#2f445d"/>
      </linearGradient>
    </defs>
    <polygon role="img" aria-label="City skyline photograph in blue tones" points="0,0 43,0 125,152 0,152" fill="url(#cityTop)"/>
    <polygon points="43,0 201,0 201,63 77,63" fill="var(--navy)"/>
    <rect x="0" y="152" width="201" height="32" fill="var(--navy)"/>
    <path role="img" aria-label="Dense city buildings photograph in blue tones" d="M0,184 H201 V238 Q201,277 163,273 L0,228 Z" fill="url(#cityLow)"/>
  </svg>
  <div class="wordmark" style="left:103px;top:26px;width:88px;font-size:12px">KORVATH</div>
  <div class="abs" style="right:13px;top:82px;text-align:right;font-size:11px;line-height:1.4;color:var(--navy)">QUARTERLY<br>REPORT</div>
  <div class="abs" style="right:13px;top:118px;font-size:3px;color:var(--navy)">WWW.KORVATH.COM</div>
  <div class="caps" style="left:15px;top:161px;font-size:5px">Delivering innovative and<br>customer-focused solutions.</div>
</section>

<!-- ========== INTRO ========== -->
<section class="page" style="left:390px;top:84px">
  <div class="label" style="left:18px;top:14px">INTRO</div>
  <svg class="fill" width="201" height="284"><path d="M0,27 H120 Q131,27 131,38 V58 Q131,73 114,73 H0 Z" fill="var(--ink)"/></svg>
  <div class="caps" style="left:18px;top:31px;width:100px;font-size:3.5px">Lorem ipsum dolor sit amet, consectetuer adipiscing elit, sed diam nonummy nibh euismod tincidunt ut laoreet dolore magna aliquam erat volutpat. Ut wisi enim ad minim veniam, quis nostrud exerci tation ullamcorper suscipit lobortis nisl ut aliquip ex ea commodo.</div>
  <div class="copy" style="left:18px;top:90px;width:70px"><p>Lorem ipsum dolor sit amet, consectetuer adipiscing elit, sed diam nonummy nibh euismod tincidunt ut laoreet dolore magna aliquam erat volutpat. Ut wisi enim ad minim veniam, quis nostrud exerci tation ullamcorper suscipit lobortis nisl ut aliquip ex ea commodo consequat. Duis autem vel eum iriure dolor in hendrerit in vulputate velit esse molestie consequat, vel illum dolore eu feugiat nulla facilisis at vero eros et accumsan et iusto odio dignissim qui blandit praesent luptatum zzril delenit augue duis dolore te feugait nulla facilisi. Lorem ipsum dolor sit amet, cons ectetuer adipiscing elit, sed diam nonummy nibh</p></div>
  <div class="copy" style="left:104px;top:90px;width:70px"><p>Lorem ipsum dolor sit amet, consectetuer adipiscing elit, sed diam nonummy nibh euismod tincidunt ut laoreet dolore magna aliquam erat volutpat. Ut wisi enim ad minim veniam, quis nostrud exerci tation ullamcorper suscipit lobortis nisl ut aliquip ex ea commodo consequat. Duis autem vel eum iriure dolor in hendrerit in vulputate velit esse molestie consequat, vel illum dolore eu feugiat nulla facilisis at vero eros et accumsan et iusto odio dignissim qui blandit praesent luptatum zzril delenit augue duis dolore te feugait nulla facilisi. Lorem ipsum dolor sit amet, cons ectetuer adipiscing elit, sed diam nonummy nibh</p></div>
  <footer class="doc-foot">
    <svg class="fill" width="201" height="22"><path d="M0,22 V0 H150 Q162,0 172,7 L201,22 Z" fill="var(--navy)"/></svg>
    <span class="ref">QUARTERLY REPORT | 02</span><span class="contact">T +61 00 00 0000 | SALES@KORVATH.COM | WWW.KORVATH.COM</span><span class="rule"></span><span class="mark">KORVATH</span>
  </footer>
</section>

<!-- ========== CHARTS 01 ========== -->
<section class="page" style="left:683px;top:84px">
  <div class="label" style="left:15px;top:14px">CHARTS 01</div>
  <svg class="fill" width="201" height="284">
    <circle cx="37" cy="79" r="19" fill="none" stroke="var(--light)" stroke-width="5"/>
    <circle cx="37" cy="79" r="19" fill="none" stroke="var(--ink)" stroke-width="5" stroke-dasharray="95.5 119.4" transform="rotate(-90 37 79)"/>
    <circle cx="96" cy="79" r="19" fill="none" stroke="var(--light)" stroke-width="5"/>
    <circle cx="96" cy="79" r="19" fill="none" stroke="var(--navy)" stroke-width="5" stroke-dasharray="71.6 119.4" transform="rotate(-90 96 79)"/>
    <text x="37" y="81" font-size="6" text-anchor="middle" fill="var(--text)" font-family="Arimo, sans-serif">80%</text>
    <text x="96" y="81" font-size="6" text-anchor="middle" fill="var(--text)" font-family="Arimo, sans-serif">60%</text>
    <rect x="0" y="177" width="201" height="44" fill="var(--navy)"/>
  </svg>
  <div class="copy" style="left:19px;top:106px;width:40px">Your Text Here<br><br>Easy to change colors, photos and Text</div>
  <div class="copy" style="left:76px;top:106px;width:40px">Your Text Here<br><br>Easy to change colors, photos and Text</div>
  <div class="copy" style="left:129px;top:54px;width:67px"><p>Lorem ipsum dolor sit amet, consectetuer adipiscing elit, sed diam nonummy nibh euismod tincidunt ut laoreet dolore magna aliquam erat volutpat. Ut wisi enim ad minim veniam, quis nostrud exerci tation ullamcorper suscipit lobortis nisl ut aliquip ex ea commodo consequat. Duis autem vel eum iriure dolor in hendrerit in vulputate velit esse molestie consequat, vel illum dolore eu feugiat nulla facilisis at vero eros et accumsan et iusto odio dignissim qui blandit praesent luptatum zzril delenit augue duis dolore te feugait nulla facilisi.</p><p>Lorem ipsum dolor sit amet, cons ectetuer adipiscing elit, sed diam nonummy nibh euismod tincidunt ut laoreet dolore</p></div>
  <div class="caps" style="left:17px;top:182px;width:130px;font-size:3.5px">Lorem ipsum dolor sit amet, consectetuer adipiscing elit, sed diam nonummy nibh euismod tincidunt ut laoreet dolore magna aliquam erat volutpat. Ut wisi enim ad minim veniam, quis nostrud exerci tation ullamcorper suscipit lobortis nisl ut aliquip ex</div>
  <footer class="doc-foot">
    <svg class="fill" width="201" height="22"><path d="M0,22 V0 H150 Q162,0 172,7 L201,22 Z" fill="var(--navy)"/></svg>
    <span class="ref">QUARTERLY REPORT | 02</span><span class="contact">T +61 00 00 0000 | SALES@KORVATH.COM | WWW.KORVATH.COM</span><span class="rule"></span><span class="mark">KORVATH</span>
  </footer>
</section>

<!-- ========== CHARTS 02 ========== -->
<section class="page" style="left:944px;top:84px">
  <svg class="fill" width="201" height="284">
    <defs><linearGradient id="towersGrey" x1="0" y1="0" x2="1" y2="1"><stop offset="0" stop-color="#d9d9d9"/><stop offset=".5" stop-color="#8e8e8e"/><stop offset="1" stop-color="#4b4b4b"/></linearGradient></defs>
    <path role="img" aria-label="Upward view of glass office towers in greyscale" d="M0,0 H201 V112 Q201,124 190,121 L0,58 Z" fill="url(#towersGrey)"/>
    <g font-family="Arimo, sans-serif" font-size="2.2" fill="var(--grey-dark)">
      <line x1="22" y1="199" x2="124" y2="199" stroke="#cfcfcf" stroke-width=".3"/>
      <line x1="22" y1="191" x2="124" y2="191" stroke="#ededed" stroke-width=".3"/>
      <line x1="22" y1="183" x2="124" y2="183" stroke="#ededed" stroke-width=".3"/>
      <line x1="22" y1="175" x2="124" y2="175" stroke="#ededed" stroke-width=".3"/>
      <line x1="22" y1="167" x2="124" y2="167" stroke="#ededed" stroke-width=".3"/>
      <line x1="22" y1="159" x2="124" y2="159" stroke="#ededed" stroke-width=".3"/>
      <line x1="22" y1="151" x2="124" y2="151" stroke="#ededed" stroke-width=".3"/>
      <text x="17" y="200">0</text><text x="17" y="192">2</text><text x="17" y="184">4</text><text x="17" y="176">6</text><text x="17" y="168">8</text><text x="16" y="160">10</text><text x="16" y="152">12</text><text x="16" y="145">14</text>
      <rect x="30" y="184" width="9" height="15" fill="var(--grey)"/><rect x="30" y="170" width="9" height="14" fill="var(--navy)"/><rect x="30" y="166" width="9" height="4" fill="var(--ink)"/>
      <rect x="55" y="189" width="9" height="10" fill="var(--grey)"/><rect x="55" y="171" width="9" height="18" fill="var(--navy)"/><rect x="55" y="165" width="9" height="6" fill="var(--ink)"/>
      <rect x="80" y="185" width="9" height="14" fill="var(--grey)"/><rect x="80" y="178" width="9" height="7" fill="var(--navy)"/><rect x="80" y="167" width="9" height="11" fill="var(--ink)"/>
      <rect x="105" y="181" width="9" height="18" fill="var(--grey)"/><rect x="105" y="170" width="9" height="11" fill="var(--navy)"/><rect x="105" y="151" width="9" height="19" fill="var(--ink)"/>
      <text x="29" y="203">Category 1</text><text x="54" y="203">Category 2</text><text x="79" y="203">Category 3</text><text x="104" y="203">Category 4</text>
      <text x="54" y="207" font-size="1.9">● Series 1  ● Series 2  ● Series 3</text>
      <text x="63" y="142" font-size="3" text-anchor="middle">Chart Title</text>
    </g>
  </svg>
  <div class="label" style="left:15px;top:14px;color:#fff">CHARTS 02</div>
  <div class="abs" style="left:17px;top:107px;font-size:4.6px;line-height:1.25;color:var(--navy)">LOREM IPSUM<br>DOLOR SIT AMET,<br>CONSECTETUER</div>
  <div class="copy" style="left:17px;top:217px;width:72px">Lorem ipsum dolor sit amet, consectetuer adipiscing elit, sed diam nonummy nibh euismod tincidunt ut laoreet dolore magna aliquam erat volutpat. Ut wisi enim ad minim veniam, quis nostrud exerci tation ullamcorper suscipit lobortis nisl ut aliquip ex ea commodo consequat. Duis autem vel eum iriure dolor in hendrerit in vulputate</div>
  <div class="copy" style="left:106px;top:217px;width:72px">Lorem ipsum dolor sit amet, consectetuer adipiscing elit, sed diam nonummy nibh euismod tincidunt ut laoreet dolore magna aliquam erat volutpat. Ut wisi enim ad minim veniam, quis nostrud exerci tation ullamcorper suscipit lobortis nisl ut aliquip ex ea commodo consequat. Duis autem vel eum iriure dolor in hendrerit in vulputate</div>
  <footer class="doc-foot">
    <svg class="fill" width="201" height="22"><path d="M0,22 V0 H150 Q162,0 172,7 L201,22 Z" fill="var(--navy)"/></svg>
    <span class="ref">QUARTERLY REPORT | 02</span><span class="contact">T +61 00 00 0000 | SALES@KORVATH.COM | WWW.KORVATH.COM</span><span class="rule"></span><span class="mark">KORVATH</span>
  </footer>
</section>

<!-- ========== TEXT 01 ========== -->
<section class="page" style="left:71px;top:408px">
  <svg class="fill" width="201" height="284" role="img" aria-label="Ocean waves crashing on rocks photograph in blue tones">
    <defs><linearGradient id="surf" x1="0" y1="0" x2="1" y2="1"><stop offset="0" stop-color="#3b5c75"/><stop offset=".5" stop-color="#6f92aa"/><stop offset="1" stop-color="#9db7c6"/></linearGradient></defs>
    <rect width="201" height="284" fill="url(#surf)"/>
  </svg>
  <div class="abs" style="left:0;top:0;width:118px;height:262px;background:rgba(27,50,71,.78)"></div>
  <div class="label" style="left:17px;top:12px;color:#fff">TEXT 01</div>
  <div class="copy" style="left:17px;top:47px;width:92px;color:#fff"><p>Lorem ipsum dolor sit amet, consectetuer adipiscing elit, sed diam nonummy nibh euismod tincidunt ut laoreet dolore magna aliquam erat volutpat. Ut wisi enim ad minim veniam, quis nostrud exerci tation ullamcorper suscipit lobortis nisl ut aliquip ex ea commodo consequat. Duis autem vel eum iriure dolor in</p><p>hendrerit in vulputate velit esse molestie consequat, vel illum dolore eu feugiat nulla facilisis at vero eros et accumsan et iusto odio dignissim qui blandit praesent luptatum zzril delenit augue duis dolore te feugait nulla facilisi.</p><p>Lorem ipsum dolor sit amet, cons ectetuer adipiscing elit, sed diam nonummy nibh euismod tincidunt ut laoreet dolore Lorem ipsum dolor sit amet, consectetuer adipiscing elit, sed diam nonummy nibh euismod tincidunt ut laoreet dolore magna aliquam erat volutpat. Ut wisi enim ad minim veniam, quis nostrud exerci tation ullamcorper suscipit lobortis nisl ut aliquip ex ea commodo consequat. Duis autem vel eum iriure dolor in hendrerit in vulputate velit esse molestie consequat, vel illum dolore eu feugiat nulla facilisis at vero eros et accumsan et iusto odio dignissim qui blandit praesent luptatum zzril delenit augue duis dolore te feugait nulla facilisi.</p></div>
  <footer class="doc-foot">
    <svg class="fill" width="201" height="22"><path d="M0,22 V0 H150 Q162,0 172,7 L201,22 Z" fill="var(--navy)"/></svg>
    <span class="ref">QUARTERLY REPORT | 02</span><span class="contact">T +61 00 00 0000 | SALES@KORVATH.COM | WWW.KORVATH.COM</span><span class="rule"></span><span class="mark">KORVATH</span>
  </footer>
</section>

<!-- ========== CHARTS 03 ========== -->
<section class="page" style="left:390px;top:408px">
  <div class="label" style="left:15px;top:14px">CHARTS 03</div>
  <div class="copy" style="left:15px;top:26px;width:172px"><p>Lorem ipsum dolor sit amet, consectetuer adipiscing elit, sed diam nonummy nibh euismod tincidunt ut laoreet dolore magna aliquam erat volutpat. Ut wisi enim ad minim veniam, quis nostrud exerci tation ullamcorper suscipit Lorem ipsum dolor sit amet, consectetuer adipiscing elit, sed diam nonummy nibh euismod tincidunt ut l</p><p>aoreet dolore magna aliquam erat volutpat. Ut wisi enim ad minim veniam, quis nostrud exerci tation ullamcorper suscipit</p></div>
  <svg class="fill" width="201" height="284" font-family="Arimo, sans-serif">
    <text x="50" y="76" font-size="4.6" text-anchor="middle" fill="var(--grey-dark)">Sales</text>
    <text x="141" y="76" font-size="4.6" text-anchor="middle" fill="var(--grey-dark)">Sales</text>
    <g transform="translate(50 117)" stroke="#fff" stroke-width=".4">
      <path d="M0,0 L0,-36 A36,36 0 1 1 -21.2,29.1 Z" fill="var(--navy)"/>
      <path d="M0,0 L-21.2,29.1 A36,36 0 0 1 -29.1,-21.2 Z" fill="#858585"/>
      <path d="M0,0 L-29.1,-21.2 A36,36 0 0 1 -11.1,-34.2 Z" fill="var(--grey-dark)"/>
      <path d="M0,0 L-11.1,-34.2 A36,36 0 0 1 0,-36 Z" fill="var(--navy-soft)"/>
    </g>
    <g transform="translate(141 117)" stroke="#fff" stroke-width=".4">
      <path d="M0,0 L0,-36 A36,36 0 1 1 -21.2,29.1 Z" fill="var(--navy)"/>
      <path d="M0,0 L-21.2,29.1 A36,36 0 0 1 -29.1,-21.2 Z" fill="#858585"/>
      <path d="M0,0 L-29.1,-21.2 A36,36 0 0 1 -11.1,-34.2 Z" fill="var(--grey-dark)"/>
      <path d="M0,0 L-11.1,-34.2 A36,36 0 0 1 0,-36 Z" fill="var(--navy-soft)"/>
    </g>
  </svg>
  <div class="legend" style="left:14px;top:157px"><i style="background:var(--navy)"></i>1st Qtr<i style="background:#858585"></i>2nd Qtr<i style="background:#d9a43a"></i>3rd Qtr<i style="background:#d9a43a"></i>4th Qtr</div>
  <div class="legend" style="left:105px;top:157px"><i style="background:var(--navy)"></i>1st Qtr<i style="background:#858585"></i>2nd Qtr<i style="background:#d9a43a"></i>3rd Qtr<i style="background:#d9a43a"></i>4th Qtr</div>
  <div class="copy" style="left:15px;top:171px;width:70px">Lorem ipsum dolor sit amet, consectetuer adipiscing elit, sed diam nonummy nibh euismod tincidunt ut laoreet dolore magna aliquam erat volutpat. Ut wisi enim ad minim veniam, quis nostrud exerci tation ullamcorper suscipit</div>
  <div class="copy" style="left:108px;top:171px;width:70px">Lorem ipsum dolor sit amet, consectetuer adipiscing elit, sed diam nonummy nibh euismod tincidunt ut laoreet dolore magna aliquam erat volutpat. Ut wisi enim ad minim veniam, quis nostrud exerci tation ullamcorper suscipit</div>
  <footer class="doc-foot">
    <svg class="fill" width="201" height="22"><path d="M0,22 V0 H150 Q162,0 172,7 L201,22 Z" fill="var(--navy)"/></svg>
    <span class="ref">QUARTERLY REPORT | 02</span><span class="contact">T +61 00 00 0000 | SALES@KORVATH.COM | WWW.KORVATH.COM</span><span class="rule"></span><span class="mark">KORVATH</span>
  </footer>
</section>

<!-- ========== CHARTS 04 ========== -->
<section class="page" style="left:683px;top:408px">
  <div class="label" style="left:15px;top:14px">CHARTS 04</div>
  <table class="data-table">
    <tr><th class="first">xxx</th><th class="num">xxx</th><th class="num">xxx</th><th class="num">xxx</th><th class="num">Total</th></tr>
    <tr><td class="name">Shopping</td><td>66.4%</td><td>73.2%</td><td>79.5%</td><td>73.4%</td></tr>
    <tr><td class="name">Treatment</td><td>6.4%</td><td>8.0%</td><td>14.2%</td><td>9.7%</td></tr>
    <tr><td class="name">Other</td><td>6.4%</td><td>3.6%</td><td>4.7%</td><td>3.2%</td></tr>
    <tr><td class="name">Shopping</td><td>14.5%</td><td>7.1%</td><td>.8%</td><td>8.6%</td></tr>
    <tr><td class="name">Treatment</td><td></td><td>.9%</td><td>.8%</td><td>.3%</td></tr>
    <tr><td class="name">Other</td><td>.9%</td><td>1.8%</td><td></td><td>1.1%</td></tr>
    <tr><td class="name">Shopping</td><td>5.5%</td><td>5.4%</td><td></td><td>3.7%</td></tr>
  </table>
  <div class="abs" style="left:0;top:117px;width:67px;height:103px;background:var(--navy)"></div>
  <div class="copy" style="left:6px;top:120px;width:55px;color:#fff">Lorem ipsum dolor sit amet, consectetuer adipiscing elit, sed diam nonummy nibh euismod tincidunt ut laoreet dolore magna aliquam erat volutpat. Ut wisi enim ad minim veniam, quis nostrud exerci tation ullamcorper suscipit lobortis nisl ut aliquip ex ea commodo consequat. Duis autem vel eu<br><br>m iriure dolor in hendrerit in vulputate velit esse molestie consequat, vel illum dolore eu feugiat nulla facilisis at vero eros et accumsan et iusto odio dignissim qui blandit praesent luptatum zzril</div>
  <div class="copy" style="left:74px;top:119px;width:112px"><p>Lorem ipsum dolor sit amet, consectetuer adipiscing elit, sed diam nonummy nibh euismod tincidunt ut laoreet dolore magna aliquam erat volutpat. Ut wisi enim ad minim veniam, quis nostrud exerci tation ullamcorper suscipit lobortis nisl ut aliquip ex ea commodo consequat. Duis autem vel eu</p><p>m iriure dolor in hendrerit in vulputate velit esse molestie consequat, vel illum dolore eu feugiat nulla facilisis at vero eros et accumsan et iusto odio dignissim qui blandit praesent luptatum zzril delenit augue duis dolore te feugait nulla facilisi.</p><p>Lorem ipsum dolor sit amet, cons ectetuer adipiscing elit, sed diam nonummy nibh euismod tincidunt ut laoreet dolore magna aliquam erat volutpat. Ut wisi enim ad minim veniam, quis nostrud exerci tation ullamcorper suscipit lobortis nisl ut aliquip ex ea commodo consequat. Lorem ipsum dolor s</p></div>
  <footer class="doc-foot">
    <svg class="fill" width="201" height="22"><path d="M0,22 V0 H150 Q162,0 172,7 L201,22 Z" fill="var(--navy)"/></svg>
    <span class="ref">QUARTERLY REPORT | 02</span><span class="contact">T +61 00 00 0000 | SALES@KORVATH.COM | WWW.KORVATH.COM</span><span class="rule"></span><span class="mark">KORVATH</span>
  </footer>
</section>

<!-- ========== TEXT 03 ========== -->
<section class="page" style="left:944px;top:412px">
  <div class="label" style="left:15px;top:14px">TEXT 03</div>
  <svg class="abs" style="left:0;top:29px" width="114" height="71" role="img" aria-label="Ocean wave photograph"><defs><linearGradient id="wave3" x1="0" y1="0" x2="1" y2="1"><stop offset="0" stop-color="#5d7f98"/><stop offset="1" stop-color="#2c4a61"/></linearGradient></defs><rect width="114" height="71" fill="url(#wave3)"/></svg>
  <svg class="abs" style="left:0;top:102px" width="52" height="71" role="img" aria-label="Digital network glow illustration in purple"><defs><radialGradient id="net3" cx=".55" cy=".35" r=".8"><stop offset="0" stop-color="#b9a8ff"/><stop offset=".3" stop-color="#4a3a9a"/><stop offset="1" stop-color="#17173f"/></radialGradient></defs><rect width="52" height="71" fill="url(#net3)"/></svg>
  <svg class="abs" style="left:55px;top:102px" width="59" height="136" role="img" aria-label="Tall city towers photograph in blue tones"><defs><linearGradient id="tower3" x1="0" y1="0" x2="0" y2="1"><stop offset="0" stop-color="#c8d2dc"/><stop offset=".6" stop-color="#667b93"/><stop offset="1" stop-color="#3a4f67"/></linearGradient></defs><rect width="59" height="136" fill="url(#tower3)"/></svg>
  <svg class="abs" style="left:0;top:176px" width="52" height="62" role="img" aria-label="Upward view of office buildings in greyscale"><defs><linearGradient id="up3" x1="0" y1="0" x2="1" y2="1"><stop offset="0" stop-color="#cfcfcf"/><stop offset="1" stop-color="#4f4f4f"/></linearGradient></defs><rect width="52" height="62" fill="url(#up3)"/></svg>
  <div class="tick-item" style="top:30px"><div class="head"><svg width="5" height="5"><circle cx="2.5" cy="2.5" r="2.5" fill="var(--navy)"/><path d="M1.2,2.6 L2.2,3.5 L3.8,1.6" stroke="#fff" stroke-width=".6" fill="none"/></svg>Opportunities</div><div class="copy">Lorem ipsum dolor sit amet, consectetuer adipiscing elit, sed diam nonummy nibh euismod tincidunt ut laoreet dolore magna aliquam erat volutpat. Ut wisi enim ad minim veniam, quis nostrud exerci tation ullamcorper st, vel illum dolore eu feugiat nulla facilisis</div></div>
  <div class="tick-item" style="top:79px"><div class="head"><svg width="5" height="5"><circle cx="2.5" cy="2.5" r="2.5" fill="var(--navy)"/><path d="M1.2,2.6 L2.2,3.5 L3.8,1.6" stroke="#fff" stroke-width=".6" fill="none"/></svg>Opportunities</div><div class="copy">Lorem ipsum dolor sit amet, consectetuer adipiscing elit, sed diam nonummy nibh euismod tincidunt ut laoreet dolore magna aliquam erat volutpat. Ut wisi enim ad minim veniam, quis nostrud exerci tation ullamcorper st, vel illum dolore eu feugiat nulla facilisis</div></div>
  <div class="tick-item" style="top:128px"><div class="head"><svg width="5" height="5"><circle cx="2.5" cy="2.5" r="2.5" fill="var(--navy)"/><path d="M1.2,2.6 L2.2,3.5 L3.8,1.6" stroke="#fff" stroke-width=".6" fill="none"/></svg>Opportunities</div><div class="copy">Lorem ipsum dolor sit amet, consectetuer adipiscing elit, sed diam nonummy nibh euismod tincidunt ut laoreet dolore magna aliquam erat volutpat. Ut wisi enim ad minim veniam, quis nostrud exerci tation ullamcorper st, vel illum dolore eu feugiat nulla facilisis</div></div>
  <div class="tick-item" style="top:177px"><div class="head"><svg width="5" height="5"><circle cx="2.5" cy="2.5" r="2.5" fill="var(--navy)"/><path d="M1.2,2.6 L2.2,3.5 L3.8,1.6" stroke="#fff" stroke-width=".6" fill="none"/></svg>Opportunities</div><div class="copy">Lorem ipsum dolor sit amet, consectetuer adipiscing elit, sed diam nonummy nibh euismod tincidunt ut laoreet dolore magna aliquam erat volutpat. Ut wisi enim ad minim veniam, quis nostrud exerci tation ullamcorper st, vel illum dolore eu feugiat nulla facilisis</div></div>
  <footer class="doc-foot">
    <svg class="fill" width="201" height="22"><path d="M0,22 V0 H150 Q162,0 172,7 L201,22 Z" fill="var(--navy)"/></svg>
    <span class="ref">QUARTERLY REPORT | 02</span><span class="contact">T +61 00 00 0000 | SALES@KORVATH.COM | WWW.KORVATH.COM</span><span class="rule"></span><span class="mark">KORVATH</span>
  </footer>
</section>

<!-- ========== SLIDE: BUSINESS SUMMARY ========== -->
<section class="slide" style="left:71px;top:725px">
  <svg class="fill" width="324" height="182">
    <defs><linearGradient id="skyline1" x1="0" y1="0" x2="0" y2="1"><stop offset="0" stop-color="#d3dbe3"/><stop offset=".5" stop-color="#7f92a8"/><stop offset="1" stop-color="#3d5269"/></linearGradient></defs>
    <rect role="img" aria-label="City skyline photograph in blue tones" width="324" height="182" fill="url(#skyline1)"/>
    <polygon points="242,0 324,0 324,182 165,182" fill="var(--ink)"/>
    <rect x="220" y="52" width="104" height="40" fill="var(--navy)"/>
  </svg>
  <div class="wordmark" style="left:220px;top:66px;width:104px;font-size:11px">KORVATH</div>
  <div class="abs" style="left:249px;top:110px;font-size:10.5px;line-height:1.3;color:#fff;letter-spacing:.3px">BUSINESS<br>SUMMARY</div>
</section>

<!-- ========== SLIDE: AGENDA ========== -->
<section class="slide" style="left:446px;top:725px">
  <div class="slide-title" style="color:var(--ink)">AGENDA</div>
  <svg class="fill" width="324" height="182">
    <defs><radialGradient id="globe" cx=".6" cy=".35" r=".75"><stop offset="0" stop-color="#c9b8ff"/><stop offset=".2" stop-color="#5a44b0"/><stop offset=".7" stop-color="#262063"/><stop offset="1" stop-color="#14163c"/></radialGradient></defs>
    <path role="img" aria-label="Digital world network illustration in deep purple" d="M182,0 H324 V182 H140 C148,110 160,40 182,0 Z" fill="url(#globe)"/>
    <rect x="13" y="30" width="16" height="152" fill="var(--navy)"/>
    <line x1="39" y1="131" x2="64" y2="131" stroke="var(--navy)" stroke-width=".4"/>
  </svg>
  <div class="agenda-nums">02<br>03<br>04<br>05<br>06<br>07<br>08<br>09<br>10<br>11<br>12<br>13</div>
  <div class="agenda-list">VISION<br>ABOUT<br>OUR TEAM<br>SUMMARY<br>VISION<br>ABOUT<br>OUR TEAM<br>SUMMARY<br>VISION<br>ABOUT<br>OUR TEAM<br>SUMMARY</div>
  <div class="logo-box">KORVATH</div>
</section>

<!-- ========== SLIDE: ABOUT US ========== -->
<section class="slide" style="left:821px;top:733px;background:var(--ink)">
  <svg class="abs" style="left:148px;top:0" width="176" height="182" role="img" aria-label="Upward view of office towers in greyscale"><defs><radialGradient id="towersUp" cx=".5" cy=".45" r=".7"><stop offset="0" stop-color="#f2f2f2"/><stop offset=".5" stop-color="#9a9a9a"/><stop offset="1" stop-color="#3e3e3e"/></radialGradient></defs><rect width="176" height="182" fill="url(#towersUp)"/></svg>
  <div class="slide-title" style="color:#fff;font-size:8.8px">ABOUT US</div>
  <div class="caps" style="left:17px;top:48px;width:110px;font-size:4.4px">Lorem ipsum dolor sit amet, consectetuer adipiscing elit, sed diam nonummy nibh euismod tincidunt ut laoreet</div>
  <div class="copy" style="left:17px;top:93px;width:62px;color:#fff">Lorem ipsum dolor sit amet, consectetuer adipiscing elit, sed diam nonummy nibh euismod tincidunt ut laoreet dolore magna aliquam erat volutpat. Ut wisi enim ad minim veniam, quis nostrud exerci tation ullamcorper suscipit lobortis nisl ut aliquip ex ea commodo consequat. Duis autem vel eum iriure dolor in hendrerit in vulputate velit esse molestie consequat, vel illum dolore eu feugiat nulla facilisis at vero eros et accumsan et iusto odio dignissim qui blandit praesent luptatum zzril</div>
  <div class="copy" style="left:85px;top:93px;width:62px;color:#fff">Lorem ipsum dolor sit amet, consectetuer adipiscing elit, sed diam nonummy nibh euismod tincidunt ut laoreet dolore magna aliquam erat volutpat. Ut wisi enim ad minim veniam, quis nostrud exerci tation ullamcorper suscipit lobortis nisl ut aliquip ex ea commodo consequat. Duis autem vel eum iriure dolor in hendrerit in vulputate velit esse molestie consequat, vel illum dolore eu feugiat nulla facilisis at vero eros et accumsan et iusto odio dignissim qui blandit praesent luptatum zzril</div>
  <div class="logo-box">KORVATH</div>
</section>

<!-- ========== SLIDE: OBJECTIVES ========== -->
<section class="slide" style="left:71px;top:934px">
  <div class="abs" style="left:102px;top:0;width:79px;height:182px;background:var(--light)"></div>
  <div class="slide-title" style="color:var(--ink)">OBJECTIVES AND SUCCESS CRITERIA</div>
  <div class="abs" style="left:17px;top:35px;font-size:5.5px;color:var(--ink)">1.</div>
  <div class="abs" style="left:111px;top:35px;font-size:5.5px;color:var(--ink)">2.</div>
  <div class="abs" style="left:206px;top:35px;font-size:5.5px;color:var(--ink)">3.</div>
  <div class="copy" style="left:17px;top:48px;width:72px;font-size:4.1px">Lorem ipsum dolor sit amet, consectetuer adipiscing elit, sed diam nonummy nibh euismod tincidunt ut laoreet dolore</div>
  <div class="copy" style="left:111px;top:48px;width:72px;font-size:4.1px">Lorem ipsum dolor sit amet, consectetuer adipiscing elit, sed diam nonummy nibh euismod tincidunt ut laoreet dolore</div>
  <div class="copy" style="left:206px;top:48px;width:72px;font-size:4.1px">Lorem ipsum dolor sit amet, consectetuer adipiscing elit, sed diam nonummy nibh euismod tincidunt ut laoreet dolore</div>
  <svg class="fill" width="324" height="182" fill="none" stroke="#fff" stroke-width=".6">
    <polygon points="17,81 49,81 79,110 79,182 17,182" fill="var(--ink)" stroke="none"/>
    <polygon points="111,81 143,81 173,110 173,182 111,182" fill="var(--navy)" stroke="none"/>
    <polygon points="206,81 238,81 268,110 268,182 206,182" fill="var(--ink)" stroke="none"/>
    <circle cx="32" cy="102" r="4"/><circle cx="32" cy="102" r="1.5"/>
    <circle cx="126" cy="100" r="2.5"/><path d="M121,105 Q126,109 131,105"/>
    <path d="M216,101 Q221,95 226,101 Z"/><path d="M221,101 V106 Q221,108 219,107"/>
    <line x1="27" y1="113" x2="37" y2="113"/><line x1="121" y1="113" x2="131" y2="113"/><line x1="216" y1="113" x2="226" y2="113"/>
  </svg>
  <div class="card-text" style="left:27px;top:117px">Lorem ipsum<br>dolor sit amet,<br>consectetuer</div>
  <div class="card-text" style="left:121px;top:117px">Lorem ipsum<br>dolor sit amet,<br>consectetuer</div>
  <div class="card-text" style="left:216px;top:117px">Lorem ipsum<br>dolor sit amet,<br>consectetuer</div>
  <div class="logo-box" style="width:31px">KORVATH</div>
</section>

<!-- ========== SLIDE: SOLUTION ========== -->
<section class="slide" style="left:446px;top:934px;background:var(--ink)">
  <svg class="fill" width="324" height="182">
    <defs>
      <linearGradient id="sea" x1="0" y1="0" x2="0" y2="1"><stop offset="0" stop-color="#a9c2cf"/><stop offset=".5" stop-color="#5f8299"/><stop offset="1" stop-color="#2c4b61"/></linearGradient>
      <linearGradient id="circCity" x1="0" y1="0" x2="0" y2="1"><stop offset="0" stop-color="#d0d9e2"/><stop offset="1" stop-color="#4a6079"/></linearGradient>
      <radialGradient id="circUp"><stop offset="0" stop-color="#f0f0f0"/><stop offset="1" stop-color="#4a4a4a"/></radialGradient>
    </defs>
    <path role="img" aria-label="Open ocean waves photograph in blue tones" d="M245,0 H324 V182 H176 C178,90 200,25 245,0 Z" fill="url(#sea)"/>
    <circle role="img" aria-label="City towers photograph" cx="50" cy="132" r="33" fill="url(#circCity)"/>
    <circle role="img" aria-label="Upward view of office towers in greyscale" cx="130" cy="132" r="33" fill="url(#circUp)"/>
  </svg>
  <div class="slide-title" style="color:#fff">SOLUTION</div>
  <div class="caps" style="left:17px;top:30px;width:150px;font-size:5px;line-height:1.25">Lorem ipsum dolor sit amet, consectetuer adipiscing elit, sed diam nonummy nibh euismod tincidunt ut laoreet dolore magna aliquam erat</div>
  <div class="copy" style="left:17px;top:69px;width:140px;color:#fff;font-size:3.4px">Lorem ipsum dolor sit amet, consectetuer adipiscing elit, sed diam nonummy nibh euismod tincidunt ut laoreet dolore magna aliquam erat volutpat. Ut wisi enim ad minim veniam, quis nostrud exerci tation ullamcorper suscipit lobo</div>
  <div class="logo-box">KORVATH</div>
</section>

<!-- ========== SLIDE: WHY THIS SOLUTION ========== -->
<section class="slide" style="left:821px;top:936px">
  <div class="slide-title" style="color:var(--ink)">WHY THIS SOLUTION</div>
  <svg class="fill" width="324" height="182" fill="none" stroke="#fff" stroke-width=".6">
    <line x1="17" y1="54" x2="307" y2="54" stroke="#cfcfcf" stroke-width=".5"/>
    <circle cx="75" cy="54" r="1.2" fill="#9a9a9a" stroke="none"/><circle cx="162" cy="54" r="1.2" fill="#9a9a9a" stroke="none"/><circle cx="242" cy="54" r="1.2" fill="#9a9a9a" stroke="none"/>
    <circle cx="23" cy="42" r="7" fill="var(--ink)" stroke="none"/><path d="M20,44 A3.5,3.5 0 1 1 26,41"/><path d="M26,38.8 V41.2 H23.6"/>
    <circle cx="102" cy="42" r="7" fill="var(--ink)" stroke="none"/><circle cx="102" cy="40.5" r="2.3"/><line x1="101" y1="43.5" x2="103" y2="43.5"/><line x1="101.2" y1="45" x2="102.8" y2="45"/>
    <circle cx="187" cy="42" r="7" fill="var(--ink)" stroke="none"/><path d="M183,42 L186,40 L189,41 L191,42 L188,44.5 L185,43.5 Z" fill="#fff" stroke="none"/>
    <circle cx="262" cy="42" r="7" fill="var(--ink)" stroke="none"/><circle cx="262" cy="42" r="3.5"/><ellipse cx="262" cy="42" rx="1.5" ry="3.5"/><line x1="258.5" y1="42" x2="265.5" y2="42"/>
    <rect x="0" y="112" width="324" height="43" fill="var(--ink)" stroke="none"/>
  </svg>
  <div class="copy" style="left:17px;top:62px;width:62px;font-size:3.6px">Lorem ipsum dolor sit amet, consectetuer adipiscing elit, sed diam nonummy nibh euismod tincidunt ut laoreet dolore magna aliquam erat volutpat. Ut wisi enim ad minim veniam, quis nostrud exerci tation ullamcorper s</div>
  <div class="copy" style="left:97px;top:62px;width:62px;font-size:3.6px">Lorem ipsum dolor sit amet, consectetuer adipiscing elit, sed diam nonummy nibh euismod tincidunt ut laoreet dolore magna aliquam erat volutpat. Ut wisi enim ad minim veniam, quis nostrud exerci tation ullamcorper s</div>
  <div class="copy" style="left:181px;top:62px;width:62px;font-size:3.6px">Lorem ipsum dolor sit amet, consectetuer adipiscing elit, sed diam nonummy nibh euismod tincidunt ut laoreet dolore magna aliquam erat volutpat. Ut wisi enim ad minim veniam, quis nostrud exerci tation ullamcorper s</div>
  <div class="copy" style="left:256px;top:62px;width:58px;font-size:3.6px">Lorem ipsum dolor sit amet, consectetuer adipiscing elit, sed diam nonummy nibh euismod tincidunt ut laoreet dolore magna aliquam erat volutpat. Ut wisi enim ad minim veniam, quis nostrud exerci tation ullamcorper s</div>
  <div class="copy" style="left:17px;top:118px;width:290px;color:#fff;font-size:3.4px"><p>Lorem ipsum dolor sit amet, consectetuer adipiscing elit, sed diam nonummy nibh euismod tincidunt ut laoreet dolore magna aliquam erat volutpat. Ut wisi enim ad minim veniam, quis nostrud exerci tation ullamcorper s</p><p>uscipit lobortis nisl ut aliquip ex ea commodo consequat. Duis autem vel eum iriure dolor in hendrerit in vulputate velit esse molestie consequat, vel illum dolore eu feugiat nulla facilisis at vero eros et</p></div>
  <div class="logo-box">KORVATH</div>
</section>

</div>
</body>
</html>
```